All Natural Mosquito Repellent

My company, BrightFern Company has created an all natural mosquito repellent. I already have other all natural products that I have developed and created labels for. I will include a copy of that label so you have something to work from. I will need two labels. One for the front of the bottle and one for the back. The back label will need space for a UPC. The labels need to be 63mm (H) x 39mm (W)

Target Market(s)

Consumers, Organic, People who like natural products

Font styles to use
Other font styles liked:
• A combination of both Serif and Sans Serif

Requirements
Must have
• Use the words Organic, All Natural, Travel size, made in the USA label
Nice to have
• tag line: Don't beat them off. Spray them away.

```html
<!DOCTYPE html>
<html lang="en">
<head>
<meta charset="utf-8">
<title>BrightFern Co. – Mosquito Repellent Labels</title>
<link href="https://fonts.googleapis.com/css2?family=Alfa+Slab+One&family=Roboto+Slab:wght@400;700&family=Roboto+Condensed:wght@400;700&family=Playfair+Display:ital@1&display=swap" rel="stylesheet">
<style>
  :root {
    --bg: #bcbdc0;
    --label: #141515;
    --label-edge: #232525;
    --green: #1f9a62;
    --green-dark: #137045;
    --white: #f2f2f2;
    --muted: #8a8c8e;
    --red: #c8262c;
    --navy: #27346b;
  }
  * { box-sizing: border-box; margin: 0; padding: 0; }
  html, body { width: 1141px; height: 1200px; overflow: hidden; }
  body { background: var(--bg); position: relative; font-family: "Roboto Slab", serif; color: var(--white); }

  .label {
    position: absolute; top: 287px; width: 500px; height: 625px;
    background: var(--label); overflow: hidden;
    box-shadow: 0 0 0 1px var(--label-edge);
  }
  .label--front { left: 47px; }
  .label--back { left: 594px; }

  .brand {
    position: absolute; left: 0; right: 0; display: flex; justify-content: center; align-items: center; gap: 10px;
    font-family: "Roboto Condensed", sans-serif; font-weight: 400; font-size: 38px; color: var(--white); letter-spacing: 0.5px;
  }
  .brand__dot { width: 38px; height: 38px; border-radius: 50%; background: var(--green); }
  .label--front .brand { top: 110px; }
  .label--back .brand { top: 70px; }

  .rule { position: absolute; height: 2px; background: #3a3c3d; }
  .label--front .rule { left: 40px; right: 40px; top: 184px; }
  .label--back .rule { left: 70px; right: 60px; top: 130px; }

  .front__title {
    position: absolute; left: 20px; top: 200px; font-family: "Alfa Slab One", serif; font-size: 80px; color: var(--green); letter-spacing: -1px; line-height: 1;
  }
  .front__icon { position: absolute; left: 420px; top: 208px; width: 80px; height: 90px; }
  .front__sub {
    position: absolute; left: 0; right: 0; top: 318px; text-align: center; font-family: "Alfa Slab One", serif; font-size: 54px; color: var(--white); line-height: 1;
  }
  .front__organic {
    position: absolute; left: 182px; width: 140px; top: 398px; text-align: center;
    font-family: "Alfa Slab One", serif; font-size: 24px; color: var(--white); padding: 6px 0;
    border-top: 2px solid var(--white); border-bottom: 2px solid var(--white); line-height: 1.1;
  }
  .front__seal { position: absolute; left: 2px; top: 410px; width: 92px; height: 92px; }
  .front__weight { position: absolute; left: 0; right: 0; top: 495px; text-align: center; }
  .front__weight-label { font-family: "Roboto Slab", serif; font-weight: 700; font-size: 18px; }
  .front__weight-value { font-family: "Roboto Slab", serif; font-weight: 700; font-size: 40px; color: var(--green); line-height: 1.1; }
  .front__travel { position: absolute; left: 430px; top: 400px; width: 70px; height: 160px; }

  .back__kicker { position: absolute; left: 0; right: 0; top: 150px; text-align: center; font-family: "Playfair Display", serif; font-style: italic; font-size: 22px; }
  .back__title { position: absolute; left: 0; right: 0; top: 180px; text-align: center; font-family: "Alfa Slab One", serif; font-size: 48px; line-height: 1; }
  .back__sub { position: absolute; left: 0; right: 0; top: 238px; text-align: center; font-family: "Alfa Slab One", serif; font-size: 26px; line-height: 1; }
  .back__copy { position: absolute; left: 8px; right: 8px; top: 282px; text-align: center; font-family: "Roboto Slab", serif; font-weight: 700; font-size: 13.5px; line-height: 1.5; }
  .back__copy p + p { margin-top: 10px; }
  .back__note { position: absolute; left: 6px; width: 240px; top: 505px; font-family: "Roboto Slab", serif; font-weight: 700; font-size: 13.5px; line-height: 1.5; }
  .back__upc { position: absolute; left: 383px; top: 478px; width: 117px; height: 125px; background: #e6e6e6; }
</style>
</head>
<body>

<section class="label label--front">
  <div class="brand"><span class="brand__dot"></span><span>BRIGHTFERN CO.</span></div>
  <div class="rule"></div>
  <h1 class="front__title">MOSQUIT</h1>
  <svg class="front__icon" viewBox="0 0 80 90" role="img" aria-label="Mosquito illustration inside a red no-entry sign">
    <circle cx="40" cy="48" r="34" fill="var(--green-dark)" stroke="var(--red)" stroke-width="7"/>
    <line x1="16" y1="24" x2="64" y2="72" stroke="var(--red)" stroke-width="7"/>
  </svg>
  <h2 class="front__sub">REPELLENT</h2>
  <div class="front__organic">ORGANIC</div>
  <svg class="front__seal" viewBox="0 0 92 92" role="img" aria-label="All natural seal">
    <circle cx="46" cy="46" r="44" fill="var(--green)"/>
  </svg>
  <div class="front__weight">
    <div class="front__weight-label">Net Weight</div>
    <div class="front__weight-value">125 ml</div>
  </div>
  <svg class="front__travel" viewBox="0 0 70 160" role="img" aria-label="Travel size and made in the USA badge">
    <rect x="8" y="0" width="62" height="60" fill="var(--green)"/>
    <rect x="0" y="66" width="70" height="94" rx="40" fill="var(--navy)"/>
  </svg>
</section>

<section class="label label--back">
  <div class="brand"><span class="brand__dot"></span><span>BRIGHTFERN CO.</span></div>
  <div class="rule"></div>
  <div class="back__kicker">all natural</div>
  <h1 class="back__title">MOSQUITO</h1>
  <h2 class="back__sub">REPELLENT</h2>
  <div class="back__copy">
    <p>Lorem ipsum dolor sit amet, consectetuer adipiscing elit, sed diam nonummy nibh euismod tincidunt ut laoreet dolore magna aliquam erat volutpat. Ut wisi enim. Lorem ipsum dolor sit amet, consectetuer adipiscing elit, sed diam nonummy nibh euismod tincidunt ut laoreet dolore magna aliquam erat volutpat. Ut wisi enim.</p>
    <p>Lorem ipsum dolor sit amet, consectetuer adipiscing elit, sed diam nonummy nibh euismod tincidunt ut laoreet dolore magna aliquam erat volutpat. Ut wisi enim. Lorem ipsum dolor sit amet, consectetuer adipiscing elit.</p>
  </div>
  <p class="back__note">Lorem ipsum dolor sit amet, consectetuer adipiscing elit, sed diam nonummy nibh euismod tincidunt ut laoreet dolore magna</p>
  <div class="back__upc" aria-label="Space for UPC"></div>
</section>

</body>
</html>
```